Eye catchy Construction Development business cards and stationery
Torvane Arch
Modern
Your Name
Managing Director
11111 My Street suite #100 City, STATE 66211
myemail@email.com
www.mywebsite.com
Use my winning logo from here http://www.plumvexstudio.com/contests/logo-for-construction-developer-company
Some elegant but modern design. One idea would be to use the company logo printed on silver metallic look, such as http://www.plumvexstudio.com/contests/theoakhearth-logo-project

```html
<!DOCTYPE html>
<html lang="en">
<head>
<meta charset="utf-8">
<title>Torvane Arch – Business Card</title>
<link rel="stylesheet" href="https://fonts.googleapis.com/css2?family=Open+Sans:wght@400;600;700&display=swap">
<style>
  :root{
    --bg:#dcdcdc;
    --card:#ffffff;
    --frame:#9a9a9a;
    --blue:#1b8cbd;
    --blue-dark:#156f97;
    --orange:#f39b1e;
    --ink:#4a4a4a;
    --ink-soft:#7a7a7a;
  }
  *{box-sizing:border-box;margin:0;padding:0}
  html,body{width:1200px;height:895px;overflow:hidden}
  body{background:var(--bg);font-family:"Open Sans",Arial,sans-serif;color:var(--ink);position:relative}
  .card{position:absolute;left:250px;width:700px;height:400px;background:var(--card);overflow:hidden;box-shadow:0 6px 18px rgba(0,0,0,.18)}
  .card--front{top:27px}
  .card--back{top:468px}
  .frame{position:absolute;inset:14px;border:1.5px solid var(--frame);z-index:3;pointer-events:none}

  .brand{position:absolute;display:flex;align-items:center;gap:12px;z-index:2}
  .brand__dot{width:46px;height:46px;border-radius:50%;background:var(--blue)}
  .brand__name{font-weight:700;font-size:30px;color:var(--blue);letter-spacing:-.3px}
  .card--front .brand{left:42px;top:42px}
  .card--back .brand{left:50%;top:120px;transform:translateX(-50%)}
  .card--back .brand__dot{width:60px;height:60px}
  .card--back .brand__name{font-size:40px}

  .contact{position:absolute;list-style:none;z-index:2}
  .contact li{display:flex;align-items:flex-start;gap:12px;font-size:15px;line-height:20px;color:var(--ink);padding:6px 0}
  .icon{width:22px;height:22px;flex:none}
  .contact--left{left:50px;top:172px}
  .contact--right{left:440px;top:240px;width:225px}

  .person{position:absolute;left:440px;top:172px;z-index:2}
  .person__name{font-size:24px;font-weight:600;color:var(--blue);line-height:32px}
  .person__role{font-size:15px;color:var(--ink-soft);margin-top:2px}

  .accent{position:absolute;left:0;top:318px;width:92px;height:18px;background:var(--orange)}
  .band{position:absolute;left:0;right:0;background:var(--blue)}
  .card--front .band{top:336px;height:34px}
  .card--back .band{top:262px;height:62px;display:flex;align-items:center;justify-content:center}
  .band__url{color:#fff;font-size:22px;font-weight:600;letter-spacing:.5px}
</style>
</head>
<body>
  <svg width="0" height="0" style="position:absolute" aria-hidden="true">
    <defs>
      <symbol id="i-phone" viewBox="0 0 22 22"><rect width="22" height="22" rx="4" fill="#1b8cbd"/><path d="M7 5h3l1 3-2 1.5a8 8 0 0 0 3.5 3.5L14 11l3 1v3a2 2 0 0 1-2 2A11 11 0 0 1 5 7a2 2 0 0 1 2-2z" fill="#fff"/></symbol>
      <symbol id="i-mail" viewBox="0 0 22 22"><rect width="22" height="22" rx="4" fill="#1b8cbd"/><rect x="4.5" y="6.5" width="13" height="9" fill="none" stroke="#fff" stroke-width="1.6"/><path d="M4.5 6.5 11 12l6.5-5.5" fill="none" stroke="#fff" stroke-width="1.6"/></symbol>
      <symbol id="i-pin" viewBox="0 0 22 22"><rect width="22" height="22" rx="4" fill="#1b8cbd"/><path d="M11 4a5 5 0 0 1 5 5c0 4-5 9-5 9s-5-5-5-9a5 5 0 0 1 5-5z" fill="#fff"/><circle cx="11" cy="9" r="2" fill="#1b8cbd"/></symbol>
      <symbol id="i-web" viewBox="0 0 22 22"><rect width="22" height="22" rx="4" fill="#1b8cbd"/><circle cx="11" cy="11" r="6" fill="none" stroke="#fff" stroke-width="1.5"/><ellipse cx="11" cy="11" rx="2.6" ry="6" fill="none" stroke="#fff" stroke-width="1.3"/><path d="M5 11h12" stroke="#fff" stroke-width="1.3"/></symbol>
    </defs>
  </svg>

  <section class="card card--front">
    <div class="frame"></div>
    <div class="brand">
      <span class="brand__dot"></span>
      <span class="brand__name">Torvane Arch</span>
    </div>

    <ul class="contact contact--left">
      <li><svg class="icon"><use href="#i-phone"/></svg>014 552 8137</li>
      <li><svg class="icon"><use href="#i-mail"/></svg>hello@torvanearch.com</li>
    </ul>

    <div class="person">
      <p class="person__name">Maren Dalloway</p>
      <p class="person__role">Production engineer</p>
    </div>

    <ul class="contact contact--right">
      <li><svg class="icon"><use href="#i-pin"/></svg><span>027 9th floor Quarry<br>Lane Road HVT</span></li>
      <li><svg class="icon"><use href="#i-web"/></svg>www.torvanearch.com</li>
    </ul>

    <div class="accent"></div>
    <div class="band"></div>
  </section>

  <section class="card card--back">
    <div class="frame"></div>
    <div class="brand">
      <span class="brand__dot"></span>
      <span class="brand__name">Torvane Arch</span>
    </div>
    <div class="band"><span class="band__url">www.torvanearch.com</span></div>
  </section>
</body>
</html>
```